Front book cover for a training course to help bakers get higher prices and sell more wedding cakes.

We need a front cover for a book that will be teaching bakers how to sell wedding cakes to get higher prices and book more orders. It is a business book. Do not make it look like we want brides to read it. Bakers will be judging the cover to see if it is worth their investment to read it. The title is already in the logo, so do not repeat it.

Target Market(s)

Bakers who sell wedding cakes

Industry/Entity Type

Bakery

Colors

Designer to choose colors to be used in the design.

Requirements
Must have
• Must use the logo. Must have author name: Lu Brandt. Must have subtitle: Boost Your Prices. Book More Brides. Build Your Empire.
Nice to have
• You are free to be creative. The concept is not to be pretty. It is a business sales and marketing book

```html
<!DOCTYPE html>
<html lang="en">
<head>
<meta charset="utf-8">
<title>Book Cover – Cake Ledger Academy</title>
<link rel="stylesheet" href="https://fonts.googleapis.com/css2?family=League+Spartan:wght@700;800&display=swap">
<style>
  :root {
    --cover-light: #fbfbfb;
    --cover-base: #ececec;
    --accent-pink: #ef4f7a;
    --ink-grey: #4d4e51;
    --paper-white: #ffffff;
    --money-green: #8fa58a;
    --money-skin: #d9a58c;
  }
  html, body {
    margin: 0;
    padding: 0;
    width: 802px;
    height: 1200px;
    overflow: hidden;
    background: var(--cover-base);
  }
  .book-cover {
    position: relative;
    width: 802px;
    height: 1200px;
    background: radial-gradient(ellipse at 50% 35%, var(--cover-light) 0%, var(--cover-base) 85%);
    font-family: "League Spartan", "Arial", sans-serif;
  }
  .cover-art {
    position: absolute;
    inset: 0;
    width: 802px;
    height: 1200px;
  }
  .headline-word { fill: var(--accent-pink); font-weight: 800; }
  .headline-sub { fill: var(--ink-grey); font-weight: 800; }
  .brand-name { fill: var(--ink-grey); font-weight: 800; }
  .author-band { fill: var(--ink-grey); }
  .author-name { fill: var(--paper-white); font-weight: 700; letter-spacing: 9px; }
</style>
</head>
<body>
<main class="book-cover">
  <svg class="cover-art" viewBox="0 0 802 1200" xmlns="http://www.w3.org/2000/svg">
    <defs>
      <linearGradient id="rule-fade" x1="0" y1="0" x2="1" y2="0">
        <stop offset="0" stop-color="var(--accent-pink)"/>
        <stop offset="0.45" stop-color="var(--accent-pink)"/>
        <stop offset="0.6" stop-color="var(--ink-grey)"/>
        <stop offset="1" stop-color="var(--ink-grey)"/>
      </linearGradient>
      <linearGradient id="money-tone" x1="0" y1="0" x2="0" y2="1">
        <stop offset="0" stop-color="var(--money-green)"/>
        <stop offset="1" stop-color="var(--money-skin)"/>
      </linearGradient>
    </defs>

    <!-- Brand name -->
    <g class="brand-lockup">
      <circle cx="214" cy="196" r="16" fill="var(--accent-pink)"/>
      <text class="brand-name" x="244" y="212" font-size="46" textLength="360" lengthAdjust="spacingAndGlyphs">Cake Ledger Academy</text>
    </g>

    <!-- Headline: Boost -->
    <text class="headline-word" x="169" y="409" font-size="140" textLength="459" lengthAdjust="spacingAndGlyphs">BOOST</text>
    <g class="growth-arrow">
      <line x1="408" y1="404" x2="472" y2="330" stroke="var(--cover-light)" stroke-width="14" stroke-linecap="butt"/>
      <line x1="412" y1="398" x2="492" y2="308" stroke="var(--accent-pink)" stroke-width="7"/>
      <polygon points="508,290 478,302 498,320" fill="var(--accent-pink)"/>
    </g>
    <text class="headline-sub" x="171" y="486" font-size="64" textLength="455" lengthAdjust="spacingAndGlyphs">YOUR PRICES.</text>
    <rect x="169" y="516" width="457" height="4" fill="url(#rule-fade)"/>

    <!-- Headline: Book -->
    <text class="headline-word" x="169" y="674" font-size="166" textLength="459" lengthAdjust="spacingAndGlyphs">BOOK</text>
    <text class="headline-sub" x="169" y="745" font-size="64" textLength="457" lengthAdjust="spacingAndGlyphs">MORE BRIDES.</text>
    <rect x="169" y="781" width="457" height="4" fill="url(#rule-fade)"/>

    <!-- Headline: Build -->
    <text class="headline-word" x="169" y="941" font-size="166" textLength="459" lengthAdjust="spacingAndGlyphs">BUILD</text>
    <g role="img" aria-label="Photo of hands holding a fan of banknotes">
      <rect x="474" y="850" width="88" height="92" rx="8" fill="url(#money-tone)"/>
    </g>
    <text class="headline-sub" x="172" y="1016" font-size="64" textLength="454" lengthAdjust="spacingAndGlyphs">YOUR EMPIRE.</text>

    <!-- Author -->
    <rect class="author-band" x="246" y="1079" width="309" height="44"/>
    <text class="author-name" x="400" y="1111" font-size="28" text-anchor="middle">LU BRANDT</text>
  </svg>
</main>
</body>
</html>
```